- Redesign our business card
- Logo remains unchanged
- Current business card attached

Target Market(s)

We are a property management company

Industry/Entity Type

Business

```html
<!DOCTYPE html>
<html lang="en">
<head>
<meta charset="utf-8">
<title>Harwood Property Group – Business Card</title>
<link href="https://fonts.googleapis.com/css2?family=Open+Sans:wght@400;600&display=swap" rel="stylesheet">
<style>
  :root {
    --page: #ffffff;
    --frame: #5a5a5a;
    --card-edge: #b9b9b9;
    --ink: #2b2b2b;
    --ink-soft: #3c3c3c;
    --brand-green: #8a9b1d;
    --brand-olive: #7f9427;
    --slate-dark: #364340;
    --slate-mid: #44524f;
    --back-text: #f2f2ee;
    --back-sub: #dcdcd6;
  }
  * { box-sizing: border-box; margin: 0; padding: 0; }
  html, body { width: 1022px; height: 1200px; overflow: hidden; background: var(--page); }
  body { font-family: "Open Sans", Arial, sans-serif; color: var(--ink); }

  .sheet {
    position: relative;
    width: 1022px; height: 1200px;
    border: 2px solid var(--frame);
    background: var(--page);
  }

  /* Front of card */
  .card-front {
    position: absolute;
    left: 63px; top: 46px;
    width: 888px; height: 486px;
    border: 1px solid var(--card-edge);
    background: #fff;
  }
  .card-front .holder-name {
    position: absolute; left: 51px; top: 86px;
    font-size: 29px; font-weight: 400; color: var(--ink);
  }
  .card-front .holder-role {
    position: absolute; left: 52px; top: 130px;
    font-size: 20px; color: var(--ink-soft);
  }
  .brand-lockup {
    position: absolute; left: 594px; top: 68px;
    display: flex; flex-direction: column; gap: 12px;
  }
  .brand-lockup .brand-square {
    width: 74px; height: 74px; background: var(--brand-green);
  }
  .brand-lockup .brand-name {
    font-size: 17px; font-weight: 400; color: var(--brand-green);
    letter-spacing: 0.5px;
  }
  .brand-lockup .brand-tag {
    font-size: 11.5px; color: var(--ink-soft); letter-spacing: 0.6px;
    margin-top: -10px;
  }
  .address-block {
    position: absolute; left: 52px; top: 236px;
    font-size: 20.5px; line-height: 34px; color: var(--ink);
  }
  .phone-block {
    position: absolute; left: 596px; top: 236px;
    font-size: 20.5px; line-height: 34px; color: var(--ink);
  }
  .phone-block .label { display: inline-block; width: 38px; }
  .services {
    position: absolute; left: 52px; top: 404px;
    font-size: 22.5px; color: var(--brand-green);
  }
  .services .divider { margin: 0 12px; }
  .card-front .base-band {
    position: absolute; left: -1px; right: -1px; bottom: -1px;
    height: 19px; background: var(--brand-green);
  }

  /* Back of card */
  .card-back {
    position: absolute;
    left: 54px; top: 631px;
    width: 895px; height: 523px;
    background: linear-gradient(135deg, var(--slate-mid) 0%, var(--slate-dark) 55%, #313d3a 100%);
    overflow: hidden;
  }
  .card-back .brand-square {
    position: absolute; left: 190px; top: 118px;
    width: 180px; height: 180px; background: var(--brand-olive);
  }
  .card-back .brand-name {
    position: absolute; left: 190px; top: 372px;
    font-size: 35px; font-weight: 400; color: var(--back-text);
    letter-spacing: 1px;
  }
  .card-back .brand-tag {
    position: absolute; left: 190px; top: 420px;
    font-size: 26px; color: var(--back-sub); letter-spacing: 1px;
  }
</style>
</head>
<body>
  <main class="sheet">
    <section class="card-front" aria-label="Business card front">
      <h1 class="holder-name">Daniel Marsh</h1>
      <p class="holder-role">Licensed Strata Manager</p>

      <div class="brand-lockup">
        <span class="brand-square" aria-hidden="true"></span>
        <span class="brand-name">HARWOOD PROPERTY GROUP</span>
        <span class="brand-tag">STRATA MANAGEMENT SERVICES</span>
      </div>

      <address class="address-block" style="font-style:normal">
        PO BOX 48, GLENHAVEN NSW 2156<br>
        12/5-19 ELLIOT LANE BRAMLEY NSW 2031<br>
        Email: info@harwoodproperty.example<br>
        www.harwoodproperty.example
      </address>

      <div class="phone-block">
        <span class="label">T:</span> 02 5550 0142<br>
        <span class="label">F:</span> 02 5550 0187<br>
        <span class="label">M:</span>0400 555 218
      </div>

      <p class="services">Strata Management<span class="divider">|</span>Community Management<span class="divider">|</span>Property Management</p>

      <div class="base-band"></div>
    </section>

    <section class="card-back" aria-label="Business card back">
      <span class="brand-square" aria-hidden="true"></span>
      <p class="brand-name">HARWOOD PROPERTY GROUP</p>
      <p class="brand-tag">STRATA MANAGEMENT SERVICES</p>
    </section>
  </main>
</body>
</html>
```